Current website re-design to a updated look and feel.

We currently have a website www.brightlanefreight.com that we want to give an updated look and feel to. We are a logistics company that competes with Falcora, Dw Hartley, Vanta but on a smaller scale. We want something fresh and updated. We have two locations one in downtown Chicago, IL and one in Palatine IL. We are a fun group that also gets the job done. We know we need pictures of both locations and possibly a video, but we need fresh design ideas. The 'who we are' page is really the only page that we currently want to keep. The 'what we do' page needs to be completely re-done from a look and feel for sure.

Target Market(s)

Anyone who uses Truck transportation to move their product. Mainly US manufacturers.

Industry/Entity Type

Logistics

Number of Pages Required

5+ page

Font styles to use
Sans Serif

Colors
5c91c4
0355a3
d0dfed

Requirements
Must have
• The new design must entice people to want to do business with us. The design must have locations for pictures and at least one video which we know we will have to provide. Design must be easy to navigate.

```html
<!DOCTYPE html>
<html lang="en">
<head>
<meta charset="utf-8">
<title>Brightlane Freight — Relax, We Got This</title>
<link rel="stylesheet" href="https://fonts.googleapis.com/css2?family=Titillium+Web:wght@400;600;700&family=Lora:wght@400;500&display=swap">
<style>
:root{
  --blue:#0355a3;
  --blue-mid:#5c91c4;
  --blue-pale:#d0dfed;
  --navy:#0b3d78;
  --ink:#333b44;
  --muted:#5a6470;
  --footer:#262a2f;
  --white:#ffffff;
}
*{box-sizing:border-box;margin:0;padding:0}
html,body{width:1200px;height:3435px;overflow:hidden;background:var(--white)}
body{font-family:"Lora",Georgia,serif;color:var(--ink);position:relative}
.abs{position:absolute}

/* header */
.topbar{top:0;left:0;width:1200px;height:92px;background:var(--white)}
.brand{left:72px;top:18px;font-family:"Titillium Web",Arial,sans-serif;font-weight:700;font-size:40px;color:var(--blue);letter-spacing:.5px}
.contact-head{top:24px;font-family:"Lora",serif;font-size:14px;color:var(--muted);line-height:20px}
.contact-head b{font-weight:400;color:var(--ink)}
.phone-ring{left:704px;top:24px;width:44px;height:44px;border-radius:50%;background:var(--blue-mid);display:flex;align-items:center;justify-content:center}
.login{left:1006px;top:24px;width:110px;height:34px;background:var(--blue);color:var(--white);font-family:"Titillium Web",sans-serif;font-weight:600;font-size:15px;display:flex;align-items:center;justify-content:center;border-radius:3px}

.nav{top:92px;left:0;width:1200px;height:45px;background:var(--blue);display:flex;align-items:center;padding-left:75px}
.nav a{font-family:"Titillium Web",sans-serif;font-weight:600;font-size:16px;color:var(--white);text-decoration:none;margin-right:42px;letter-spacing:.3px}
.nav .quote{position:absolute;right:73px;top:7px;height:32px;padding:0 18px;background:var(--blue-mid);border-radius:3px;display:flex;align-items:center;margin:0}

/* hero */
.hero{top:137px;left:0;width:1200px;height:578px;background:linear-gradient(110deg,#6d6f6a 0%,#8d8a80 25%,#4f5a63 55%,#2f3c4a 100%)}
.hero-title{left:474px;top:300px;font-family:"Lora",serif;font-size:70px;line-height:70px;color:var(--white);text-shadow:0 2px 6px rgba(0,0,0,.35)}
.dots{left:1090px;top:364px;width:38px;height:92px;border-radius:19px;background:rgba(255,255,255,.85);display:flex;flex-direction:column;align-items:center;justify-content:center;gap:8px}
.dots span{width:14px;height:14px;border-radius:50%;background:#9aa6b1}
.dots span.on{background:var(--blue)}

/* founder */
.founder-photo{left:82px;top:767px;width:90px;height:366px;background:linear-gradient(180deg,#e8e2d8 0%,#8e8b86 35%,#3b3b3d 100%);border-radius:4px}
.sec-title{font-family:"Titillium Web",sans-serif;font-weight:600;color:var(--blue);letter-spacing:.4px}
.founder-title{left:201px;top:792px;font-size:29px}
.founder-rule{left:201px;top:832px;width:916px;height:1px;background:#cfd6de}
.brand-tag{font-family:"Titillium Web",sans-serif;font-weight:700;font-size:17px;color:#1d1d1d;white-space:nowrap}
.founder-mark{left:967px;top:790px}
.founder-copy{left:201px;top:862px;width:916px;font-size:15px;line-height:25px;color:var(--muted)}
.founder-copy p{margin-bottom:18px}

/* video */
.video-band{top:1160px;left:0;width:1200px;height:500px}
.video-title{left:0;top:1240px;width:1200px;text-align:center;font-family:"Titillium Web",sans-serif;font-weight:600;font-size:25px;color:var(--white);letter-spacing:.5px}
.video-frame{left:348px;top:1287px;width:504px;height:339px;border:8px solid var(--blue-mid);background:radial-gradient(ellipse at center,#ffffff 40%,#d9dde2 100%);box-shadow:0 12px 24px rgba(0,0,0,.35);display:flex;align-items:center;justify-content:center;gap:20px}
.video-frame .name{font-family:"Titillium Web",sans-serif;font-weight:600;font-size:40px;color:var(--blue)}

/* vision */
.vm-title{left:0;top:1694px;width:1200px;text-align:center;font-size:26px}
.vm-rule{left:564px;top:1734px;width:72px;height:3px;background:var(--blue)}
.card{top:1820px;width:512px;height:275px;background:var(--blue-pale);border-radius:4px;padding:70px 40px 0;text-align:center}
.card h3{font-family:"Titillium Web",sans-serif;font-weight:700;font-size:19px;color:#1b2733;margin-bottom:14px;letter-spacing:.3px}
.card p{font-size:14px;line-height:22px;color:var(--muted)}
.badge-icon{top:1778px;width:78px;height:78px;border-radius:50%;background:var(--blue);border:5px solid var(--white);display:flex;align-items:center;justify-content:center}
.btn{background:var(--blue-mid);color:var(--white);font-family:"Titillium Web",sans-serif;font-weight:600;border-radius:3px;display:flex;align-items:center;justify-content:center}
.vm-quote{left:513px;top:2148px;width:174px;height:37px;font-size:16px;border:2px solid #a9c4df}
.vm-mark{left:967px;top:2152px}

/* services */
.services{top:2274px;left:0;width:1200px;height:566px;background:linear-gradient(180deg,var(--navy) 0%,var(--blue) 55%,#2a63a5 100%)}
.svc{top:2312px;width:244px}
.svc h4{font-family:"Titillium Web",sans-serif;font-weight:700;font-size:19px;line-height:22px;color:var(--white);height:52px;letter-spacing:.3px}
.svc .shot{width:244px;height:178px}
.svc p{margin-top:30px;font-size:13.5px;line-height:21px;color:#e6eef7;height:155px}
.svc .btn{width:112px;height:38px;font-size:14px;margin-top:10px}

/* awards */
.award-divider{left:470px;top:2876px;width:1px;height:72px;background:#b8c0c8}

/* footer */
.footer{top:2993px;left:0;width:1200px;height:442px;background:linear-gradient(180deg,#33383e 0%,var(--footer) 100%)}
.f-col{top:3038px}
.f-col h5{font-family:"Titillium Web",sans-serif;font-weight:700;font-size:16px;color:var(--white);margin-bottom:24px;letter-spacing:.3px}
.f-col li{list-style:none;font-size:14px;line-height:32px;color:#c8ccd1}
.f-text{font-size:13.5px;line-height:20px;color:#c8ccd1}
.field{height:34px;border:1px solid #5c636b;background:rgba(255,255,255,.04);font-size:13px;color:#8d949b;padding:8px 10px}
.submit{left:793px;top:3298px;width:333px;height:38px;font-size:17px;letter-spacing:.5px}
.f-rule{left:73px;top:3378px;width:1054px;height:1px;background:#4a5057}
.copy{left:73px;top:3392px;font-size:13px;color:#c8ccd1}
.social{top:3390px;width:20px;height:20px;border-radius:50%;background:#e6e6e6}
</style>
</head>
<body>

<!-- header -->
<div class="abs topbar"></div>
<div class="abs brand">Brightlane Freight</div>
<div class="abs phone-ring">
  <svg width="20" height="20" viewBox="0 0 24 24"><path d="M6.6 10.8a15.1 15.1 0 0 0 6.6 6.6l2.2-2.2c.3-.3.7-.4 1-.2 1.1.4 2.3.6 3.6.6.6 0 1 .4 1 1V20c0 .6-.4 1-1 1A17 17 0 0 1 3 4c0-.6.4-1 1-1h3.5c.6 0 1 .4 1 1 0 1.3.2 2.5.6 3.6.1.3 0 .7-.2 1z" fill="#fff"/></svg>
</div>
<div class="abs contact-head" style="left:764px">Office Phone:<br><b>847.555.0140</b></div>
<div class="abs contact-head" style="left:893px">Warehouse:<br><b>847.555.0142</b></div>
<div class="abs login">LOG IN</div>

<nav class="abs nav">
  <a>WHAT WE DO</a><a>HOW WE DO IT</a><a>WHO WE ARE</a><a>TRACKING</a><a>CHAT</a><a>CONTACT</a>
  <a class="quote">REQUSET A QUOTE</a>
</nav>

<!-- hero -->
<div class="abs hero" role="img" aria-label="Photo of a relaxed man leaning back in a wicker chair with his hands behind his head"></div>
<div class="abs hero-title">Relax<br>We Got This..</div>
<div class="abs dots"><span></span><span class="on"></span><span></span></div>

<!-- founder -->
<div class="abs founder-photo" role="img" aria-label="Full-length photo of the company founder standing in a business suit"></div>
<h2 class="abs sec-title founder-title">WELCOME FROM OUR FOUNDER</h2>
<div class="abs founder-rule"></div>
<div class="abs brand-tag founder-mark">BRIGHTLANE FREIGHT</div>
<div class="abs founder-copy">
  <p>Brightlane Freight welcomes you to our growing family of clients! We have over 26 years of experience in helping people solve their logistics needs from coast-to-coast. We also provide friendly, exceptional service that makes it easy to do business with us. Give us a call today and experience the difference for yourself!</p>
  <p>“Our service commitment begins from the moment you contact us. We appreciate your trust, and we go the extra mile to ensure that your freight is handled with care and expediency. If an issue comes up, we work tirelessly to resolve it, staying in contact with you until your freight is delivered without issue!”</p>
  <p>Let us take the worry out of your logistics. Relax, we’ve got this! – Marion Teller, Founder</p>
</div>

<!-- video -->
<svg class="abs video-band" viewBox="0 0 1200 500" role="img" aria-label="Photo of container ships loaded with cargo at a harbor">
  <defs>
    <linearGradient id="sea" x1="0" y1="0" x2="0" y2="1">
      <stop offset="0" stop-color="#8fa6b8"/>
      <stop offset=".55" stop-color="#6f8698"/>
      <stop offset="1" stop-color="#3e5566"/>
    </linearGradient>
  </defs>
  <polygon points="0,42 1200,8 1200,432 0,500" fill="url(#sea)"/>
  <polygon points="0,470 1200,400 1200,500 0,500" fill="#ffffff"/>
</svg>
<div class="abs video-title">WHACH OUR VIDEO</div>
<div class="abs video-frame">
  <span class="name">Brightlane</span>
  <svg width="84" height="84" viewBox="0 0 84 84"><circle cx="42" cy="42" r="38" fill="none" stroke="#1d1d1d" stroke-width="5"/><polygon points="33,25 62,42 33,59" fill="#1d1d1d"/></svg>
</div>

<!-- vision & mission -->
<h2 class="abs sec-title vm-title">BRIGHTLANE FREIGHT VISION AND MISSION</h2>
<div class="abs vm-rule"></div>

<div class="abs card" style="left:76px">
  <h3>BRIGHTLANE VISION</h3>
  <p>Brightlane vision is to be the premier third party logistics solution in North America. We will become premier by providing superior customer service, efficient and cost effective warehousing and distribution solutions. The decisions we make today for hiring, training, technology, strategic services and customer satisfaction are based on this vision.</p>
</div>
<div class="abs badge-icon" style="left:293px">
  <svg width="36" height="36" viewBox="0 0 36 36"><path d="M2 18C7 9 29 9 34 18 29 27 7 27 2 18z" fill="none" stroke="#fff" stroke-width="3"/><circle cx="18" cy="18" r="5.5" fill="#fff"/></svg>
</div>

<div class="abs card" style="left:614px">
  <h3>BRIGHTLANE MISSION</h3>
  <p>Brightlane’s mission is to provide the most thorough and satisfying third-party logistics experience for its customers. Brightlane uses leading technologies and an industry experienced staff to deliver an unparalleled customer service experience. Brightlane leverages the most efficient mode of transportation, and tailors cost effective solutions for warehousing and distribution of your products in every situation.</p>
</div>
<div class="abs badge-icon" style="left:831px">
  <svg width="38" height="38" viewBox="0 0 38 38"><circle cx="19" cy="19" r="14" fill="none" stroke="#fff" stroke-width="3"/><circle cx="19" cy="19" r="7" fill="none" stroke="#fff" stroke-width="3"/><circle cx="19" cy="19" r="2.5" fill="#fff"/><path d="M19 19 33 5M27 5h6v6" fill="none" stroke="#fff" stroke-width="3"/></svg>
</div>

<div class="abs btn vm-quote">REQUSIT A QUOTE</div>
<div class="abs brand-tag vm-mark">BRIGHTLANE FREIGHT</div>

<!-- services -->
<div class="abs services" role="img" aria-label="Faint background photo of a highway at night in blue tones"></div>

<div class="abs svc" style="left:73px">
  <h4>FREIGHT MANAGEMENT</h4>
  <div class="shot" role="img" aria-label="Photo of a container port with cranes and stacked containers" style="background:linear-gradient(180deg,#b9c3cc 0%,#8b7e72 55%,#4c4a4c 100%)"></div>
  <p>We strive for a perfect delivery and promise to be there for anything you may need, every step of the way. Click here to find out more about Freight Management and how we do it.</p>
  <div class="btn">Learn More</div>
</div>
<div class="abs svc" style="left:343px">
  <h4>TRANSPORTATION</h4>
  <div class="shot" role="img" aria-label="Photo of light trails on a highway at dusk" style="background:linear-gradient(180deg,#2c4a74 0%,#c7774a 45%,#3a2f35 100%)"></div>
  <p>With a combined 500+ years of industry experience between all employees, we are the logistics company you need to get the job done right. Click here to find out more about our transportation expertise.</p>
  <div class="btn">Learn More</div>
</div>
<div class="abs svc" style="left:614px">
  <h4>WAREHOUSE &amp; DISTRIBUTION</h4>
  <div class="shot" role="img" aria-label="Photo of a bright warehouse interior with stacked boxes" style="background:linear-gradient(180deg,#eef0f1 0%,#cfc7ba 60%,#a6896a 100%)"></div>
  <p>Our secure facility can accommodate large or small quantities of product. Our inventory management system provides real-time visibility.</p>
  <div class="btn">Learn More</div>
</div>
<div class="abs svc" style="left:884px">
  <h4>CARRIERS</h4>
  <div class="shot" role="img" aria-label="Photo of a red semi truck on the road under a blue sky" style="background:linear-gradient(180deg,#6ea3d6 0%,#b9d2ea 45%,#b2323a 70%,#5f6266 100%)"></div>
  <p>Are you a carrier looking to work with Brightlane? Click here to find out why we have the best carrier relationships in the business.</p>
  <div class="btn">Learn More</div>
</div>

<!-- awards -->
<div class="abs" style="left:428px;width:30px;top:2880px;height:60px;background:#1f4f86;border-radius:3px" role="img" aria-label="Business ethics award badge"></div>
<div class="abs award-divider"></div>
<div class="abs" style="left:482px;width:56px;top:2890px;height:44px;background:#c9ced4;border-radius:2px" role="img" aria-label="Award description"></div>
<div class="abs" style="left:573px;width:184px;top:2876px;height:72px;border:3px solid #1f8f86;border-radius:8px;background:#eef7f5" role="img" aria-label="Certified business enterprise badge"></div>

<!-- footer -->
<div class="abs footer" role="img" aria-label="Dark background photo of a road with street lights"></div>

<div class="abs f-col" style="left:73px">
  <h5>QUICK LINKS</h5>
  <ul><li>What We Do</li><li>How We Do It</li><li>Who We Are</li><li>Tracking</li><li>Chat</li><li>Contact</li></ul>
</div>

<div class="abs f-col" style="left:343px;width:420px">
  <h5>CONTACT US</h5>
  <div class="f-text">418 W Larch Ave. Suite 210<br>Westbrook Falls, IL 60999</div>
  <div class="f-text abs" style="top:118px;left:0">Office Phone:<br>(000) 000-0000</div>
  <div class="f-text abs" style="top:118px;left:130px">Rates:<br>rates@brightlanefreight.com</div>
  <div class="f-text abs" style="top:178px;left:0">Warehouse:<br>847.555.0142</div>
  <div class="f-text abs" style="top:178px;left:130px">Warehouse:<br>warehouse@brightlanefreight.com</div>
  <div class="f-text abs" style="top:240px;left:0">Fax:<br>847.555.0141</div>
  <div class="f-text abs" style="top:240px;left:130px">Information:<br>info@brightlanefreight.com</div>
</div>

<div class="abs f-col" style="left:790px;width:336px">
  <h5>GET UPDATES</h5>
  <div class="f-text">We occasionally send out news and related industry articles. Sign up and we promise to deliver quality information to you.</div>
</div>
<div class="abs field" style="left:793px;top:3166px;width:158px">First Name</div>
<div class="abs field" style="left:968px;top:3166px;width:158px">Last Name</div>
<div class="abs field" style="left:793px;top:3210px;width:333px">Organization</div>
<div class="abs field" style="left:793px;top:3254px;width:333px">Email</div>
<div class="abs btn submit">SUBMIT</div>

<div class="abs f-rule"></div>
<div class="abs copy">© 2017 Brightlane Freight.</div>
<div class="abs social" style="left:980px"></div>
<div class="abs social" style="left:1016px"></div>
<div class="abs social" style="left:1052px"></div>
<div class="abs social" style="left:1096px"></div>

</body>
</html>
```